Stationary design for construction company

Want professional stationary and in the future brochures to use for contacting potential customers and existing customers. We are open to suggestions with existing logo. We are a contractor in the construction field that specializes in foundation plastering. We currently do other work but are looking to market and become the only go-to subcontractor for this specialty. I like the red and black contrast and the font which is "biner d". We want to present ourselves as a professional company so potential customers take us seriously.
Brookvane Plaster
74 N. Maple #318
Orem, Utah 84092
801.555.0147 Office
801.555.0183 Mobile
maribel@brookvaneplaster.example
nolan@brookvaneplaster.example
We will need to be able to edit the finished work incase future numbers, addresses and such change.
Thx
Maribel
Target Market(s)
New and exiting customers in the building industry
Industry/Entity Type
Construction Company
Font styles to use
Other font styles liked:
- Biner D
Look and feel

```html
<!DOCTYPE html>
<html lang="en">
<head>
<meta charset="utf-8">
<title>Brookvane Plaster — Stationery</title>
<link rel="stylesheet" href="https://fonts.googleapis.com/css2?family=Roboto:wght@300;400;700&display=swap">
<style>
  :root {
    --red: #e3232c;
    --ink: #1c1c1c;
    --charcoal: #2f2f33;
    --paper: #ffffff;
    --backdrop: #ececec;
    --text: #555555;
  }
  * { box-sizing: border-box; margin: 0; padding: 0; }
  html, body { width: 806px; height: 1200px; overflow: hidden; }
  body { background: var(--backdrop); font-family: "Roboto", Arial, sans-serif; position: relative; }

  .letterhead { position: absolute; left: 46px; top: 34px; width: 719px; height: 934px; background: var(--paper); }
  .brand { position: absolute; display: flex; align-items: center; gap: 6px; }
  .brand-mark { width: 44px; height: 60px; background: var(--red); flex: none; }
  .brand-name { font-weight: 700; color: var(--ink); text-transform: uppercase; line-height: 1.05; letter-spacing: 0.5px; }
  .letterhead .brand { left: 42px; top: 42px; }
  .letterhead .brand-name { font-size: 24px; }

  .footer-rule { position: absolute; left: 0; right: 0; top: 870px; height: 2px; background: var(--red); }
  .contact { position: absolute; top: 862px; font-size: 11.5px; font-weight: 300; color: var(--text); line-height: 1.3; }
  .contact-icon { position: absolute; top: 0; width: 18px; height: 18px; background: var(--paper); border: 1.5px solid var(--red); display: flex; align-items: center; justify-content: center; }
  .contact-icon svg { width: 10px; height: 10px; fill: var(--red); }
  .contact-text { position: absolute; top: 26px; white-space: nowrap; }
  .contact-phone .contact-icon { left: 117px; } .contact-phone .contact-text { left: 74px; }
  .contact-mail .contact-icon { left: 349px; } .contact-mail .contact-text { left: 255px; top: 23px; }
  .contact-place .contact-icon { left: 585px; } .contact-place .contact-text { left: 547px; }

  .card { position: absolute; top: 1000px; width: 298px; height: 170px; background: var(--paper); overflow: hidden; }
  .card-front { left: 90px; }
  .card-back { left: 425px; }

  .card-front .band-dark { position: absolute; left: 0; right: 0; bottom: 0; height: 36px; background: var(--charcoal); }
  .card-front .bar-left { position: absolute; left: 52px; width: 60px; bottom: 16px; height: 12px; background: var(--red); }
  .card-front .bar-right { position: absolute; right: 0; width: 27px; bottom: 16px; height: 12px; background: var(--red); }
  .card-front .band-red { position: absolute; left: 101px; width: 40px; top: 0; bottom: 0; background: var(--red); }
  .rot { position: absolute; transform-origin: left top; white-space: nowrap; }
  .card-front .brand { left: 32px; top: 128px; transform: rotate(-90deg); transform-origin: left top; gap: 4px; }
  .card-front .brand-mark { width: 22px; height: 30px; }
  .card-front .brand-name { font-size: 13px; }
  .band-title { left: 113px; top: 125px; transform: rotate(-90deg); color: #fff; font-size: 11px; font-weight: 700; }
  .band-badge { position: absolute; left: 113px; top: 146px; width: 16px; height: 16px; border-radius: 50%; border: 2px solid #fff; }
  .card-emails { left: 164px; top: 110px; transform: rotate(-90deg); font-size: 7px; color: var(--text); line-height: 1.2; }
  .card-address { left: 226px; top: 102px; transform: rotate(-90deg); font-size: 7px; color: var(--text); line-height: 1.2; }
  .pin { position: absolute; left: 194px; width: 16px; height: 16px; border-radius: 50% 50% 50% 0; background: var(--red); transform: rotate(-45deg); }
  .card-phones { left: 268px; top: 167px; transform: rotate(180deg); font-size: 7px; color: #fff; line-height: 1.25; }

  .card-back .edge-red { position: absolute; left: 0; top: 22px; bottom: 22px; width: 14px; background: var(--red); }
  .card-back .edge-dark { position: absolute; right: 0; top: 22px; bottom: 22px; width: 14px; background: var(--charcoal); }
  .card-back .brand { left: 70px; top: 61px; gap: 4px; }
  .card-back .brand-mark { width: 34px; height: 48px; }
  .card-back .brand-name { font-size: 19px; }
</style>
</head>
<body>
  <section class="letterhead">
    <div class="brand">
      <span class="brand-mark"></span>
      <span class="brand-name">Brookvane<br>Plaster</span>
    </div>
    <div class="footer-rule"></div>
    <div class="contact contact-phone">
      <span class="contact-icon"><svg viewBox="0 0 24 24"><path d="M6.6 10.8a15 15 0 0 0 6.6 6.6l2.2-2.2a1 1 0 0 1 1-.25 11.4 11.4 0 0 0 3.6.57 1 1 0 0 1 1 1V20a1 1 0 0 1-1 1A17 17 0 0 1 3 4a1 1 0 0 1 1-1h3.5a1 1 0 0 1 1 1c0 1.25.2 2.45.57 3.57a1 1 0 0 1-.25 1z"/></svg></span>
      <p class="contact-text">801.555.0147 Office<br>801.555.0183 Mobile</p>
    </div>
    <div class="contact contact-mail">
      <span class="contact-icon"><svg viewBox="0 0 24 24"><path d="M2 5h20v14H2zM2 5l10 8 10-8"/></svg></span>
      <p class="contact-text">maribel@brookvaneplaster.example<br>nolan@brookvaneplaster.example</p>
    </div>
    <div class="contact contact-place">
      <span class="contact-icon"><svg viewBox="0 0 24 24"><path d="M12 2a7 7 0 0 0-7 7c0 5 7 13 7 13s7-8 7-13a7 7 0 0 0-7-7zm0 9.5A2.5 2.5 0 1 1 12 6.5a2.5 2.5 0 0 1 0 5z"/></svg></span>
      <p class="contact-text">74 N. Maple #318<br>Orem, Utah 84092</p>
    </div>
  </section>

  <section class="card card-front">
    <div class="band-dark"></div>
    <div class="bar-left"></div>
    <div class="bar-right"></div>
    <div class="band-red"></div>
    <div class="brand">
      <span class="brand-mark"></span>
      <span class="brand-name">Brookvane<br>Plaster</span>
    </div>
    <p class="rot band-title">Brookvane Plaster</p>
    <span class="band-badge"></span>
    <p class="rot card-emails">maribel@brookvaneplaster.example<br>nolan@brookvaneplaster.example</p>
    <span class="pin" style="top:22px"></span>
    <span class="pin" style="top:66px"></span>
    <span class="pin" style="top:106px"></span>
    <p class="rot card-address">74 N. Maple #318<br>Orem, Utah 84092</p>
    <p class="rot card-phones">801.555.0183 Mobile<br>801.555.0147 Office</p>
  </section>

  <section class="card card-back">
    <div class="edge-red"></div>
    <div class="edge-dark"></div>
    <div class="brand">
      <span class="brand-mark"></span>
      <span class="brand-name">Brookvane<br>Plaster</span>
    </div>
  </section>
</body>
</html>
```